K&T Holdings

Design a modern simple business card. I have attached a clean version of a card we like form Marrowfield Partners another company we own. I also attached the old K&T card design and logo and a couple of ideas we had but just can't finalize on whether we like them or not. We would like to include the 20 year logo somewhere on the card.

```html
<!DOCTYPE html>
<html lang="en">
<head>
<meta charset="utf-8">
<title>K&amp;T Holdings – Business Card</title>
<link href="https://fonts.googleapis.com/css2?family=Poppins:wght@400;500;600;700&display=swap" rel="stylesheet">
<style>
  :root{
    --navy:#232263;
    --grey:#808080;
    --text-grey:#7a7a7a;
    --white:#ffffff;
    --page:#ecebe8;
  }
  *{box-sizing:border-box;margin:0;padding:0}
  html,body{width:1200px;height:900px;overflow:hidden}
  body{
    background:var(--page);
    font-family:"Poppins",sans-serif;
    display:flex;flex-direction:column;align-items:center;justify-content:center;gap:44px;
  }
  .card{
    position:relative;width:640px;height:366px;overflow:hidden;
    box-shadow:0 6px 18px rgba(0,0,0,.18);
  }

  /* Back side */
  .card--back{background:var(--navy);color:var(--white)}
  .back-marks{
    position:absolute;left:0;right:0;top:62px;
    display:flex;align-items:center;justify-content:center;gap:40px;
  }
  .brand-name{font-weight:700;font-size:72px;letter-spacing:1px;line-height:1;color:var(--white)}
  .divider{width:1px;height:120px;background:rgba(255,255,255,.7)}
  .anniversary{font-weight:600;color:var(--white);text-align:center;line-height:1}
  .anniversary__number{font-size:84px;letter-spacing:-2px}
  .anniversary__label{font-size:16px;letter-spacing:4px;margin-top:4px}
  .anniversary__years{font-size:20px;letter-spacing:2px;margin-top:8px}
  .services{position:absolute;left:0;right:0;top:248px;text-align:center}
  .services__title{font-weight:700;font-size:19px;letter-spacing:.5px}
  .services__list{font-weight:400;font-size:15px;line-height:1.35;margin-top:6px}

  /* Front side */
  .card--front{background:var(--white)}
  .front-wave{position:absolute;inset:0}
  .person{position:absolute;left:44px;top:46px}
  .person__name{font-weight:700;font-size:24px;color:var(--navy);letter-spacing:.5px;line-height:1.1}
  .person__title{font-weight:400;font-size:15px;color:var(--text-grey)}
  .front-brand{position:absolute;right:48px;top:38px;display:flex;align-items:center;gap:10px}
  .front-brand .brand-name{color:var(--navy);font-size:64px}
  .contacts{position:absolute;left:64px;top:150px;list-style:none}
  .contacts li{display:flex;align-items:center;gap:10px;font-size:15px;color:var(--text-grey);height:24px}
  .contacts svg{width:20px;height:20px;flex:none}
  .address{position:absolute;left:64px;top:238px;font-size:15px;color:var(--text-grey);line-height:1.35}
</style>
</head>
<body>

  <section class="card card--back" aria-label="Card back">
    <div class="back-marks">
      <div class="brand-name">K&amp;T</div>
      <div class="divider"></div>
      <div class="anniversary">
        <div class="anniversary__number">20</div>
        <div class="anniversary__label">YEARS</div>
        <div class="anniversary__years">2004-2024</div>
      </div>
    </div>
    <div class="services">
      <div class="services__title">INTEGRATED INDUSTRIAL SERVICES</div>
      <div class="services__list">
        Mechanical / Civil &bull; I&amp;E &bull; Fabrication<br>
        Rotating &bull; Heat Transfer Equipment
      </div>
    </div>
  </section>

  <section class="card card--front" aria-label="Card front">
    <svg class="front-wave" viewBox="0 0 640 366" preserveAspectRatio="none" aria-hidden="true">
      <path d="M0,300 C190,300 360,250 470,180 C410,240 240,306 0,318 Z" fill="var(--grey)"/>
      <path d="M0,322 C230,318 400,250 500,182 C560,140 610,122 640,114 L640,366 L0,366 Z" fill="var(--navy)"/>
    </svg>

    <div class="person">
      <div class="person__name">DANA WHITFIELD</div>
      <div class="person__title">IT Director</div>
    </div>

    <div class="front-brand">
      <div class="brand-name">K&amp;T</div>
    </div>

    <ul class="contacts">
      <li>
        <svg viewBox="0 0 20 20"><circle cx="10" cy="10" r="9" fill="none" stroke="var(--navy)" stroke-width="1.5"/><path d="M6.5 5.5l2 .3.6 2-1.2 1a6 6 0 0 0 2.6 2.6l1-1.2 2 .6.3 2c-4.5.8-8-2.7-7.3-7.3z" fill="var(--navy)"/></svg>
        555-014-2380
      </li>
      <li>
        <svg viewBox="0 0 20 20"><circle cx="10" cy="10" r="9" fill="none" stroke="var(--navy)" stroke-width="1.5"/><path d="M6.5 5.5l2 .3.6 2-1.2 1a6 6 0 0 0 2.6 2.6l1-1.2 2 .6.3 2c-4.5.8-8-2.7-7.3-7.3z" fill="var(--navy)"/></svg>
        555-017-6641
      </li>
      <li>
        <svg viewBox="0 0 20 20"><circle cx="10" cy="10" r="9" fill="none" stroke="var(--navy)" stroke-width="1.5"/><rect x="5.5" y="7" width="9" height="6.5" fill="none" stroke="var(--navy)" stroke-width="1.2"/><path d="M5.5 7l4.5 3.6L14.5 7" fill="none" stroke="var(--navy)" stroke-width="1.2"/></svg>
        dwhitfield@ktholdings.net
      </li>
    </ul>

    <div class="address">
      128 Cedar Avenue, Suite 40<br>
      Lakeview, TX 77500
    </div>
  </section>

</body>
</html>
```